PELDRAX Business Cards

We require a business card for our company that provides IT consulting services. We already have a logo that needs to be used on the card. We want a clean professional looking design that incorporates our colours. Our main focus is providing managed services to business, which involves us looking after all of their IT requirements including managing servers/networks, projects, and procurement.

Industry/Entity Type

Information Technology

Requirements
Must have
• our logo, contact information, name, title, phone numbers

```html
<!DOCTYPE html>
<html lang="en">
<head>
<meta charset="utf-8">
<title>PELDRAX Business Card</title>
<link rel="stylesheet" href="https://fonts.googleapis.com/css2?family=Open+Sans:wght@400;600;700&family=Noto+Serif:wght@400&display=swap">
<style>
  :root {
    --page-bg: #e4e9ec;
    --brand-blue: #0093cc;
    --brand-blue-soft: #0a9bd2;
    --card-white: #ffffff;
    --panel-grey: #eeeeef;
    --base-strip: #484848;
    --ink: #111111;
  }
  * { margin: 0; padding: 0; box-sizing: border-box; }
  html, body {
    width: 1001px; height: 1200px; overflow: hidden;
    background: var(--page-bg);
  }
  .canvas { position: relative; width: 1001px; height: 1200px; }
  .card {
    position: absolute; left: 183px; width: 634px; height: 364px;
    overflow: hidden;
  }
  .card::after {
    content: ""; position: absolute; left: 0; right: 0; bottom: 0;
    height: 9px; background: var(--base-strip);
  }
  .card-front {
    top: 175px;
    background: linear-gradient(135deg, var(--brand-blue) 0%, var(--brand-blue-soft) 55%, var(--brand-blue) 100%);
  }
  .wordmark {
    position: absolute; left: 0; right: 0; top: 0; bottom: 9px;
    display: flex; align-items: center; justify-content: center; gap: 18px;
    font-family: "Open Sans", sans-serif; font-weight: 600;
    letter-spacing: 4px;
  }
  .wordmark-front { color: var(--card-white); font-size: 56px; }
  .mark-dot { display: block; flex: none; }
  .card-back { top: 661px; background: var(--panel-grey); }
  .logo-panel {
    position: absolute; left: 0; top: 0; width: 256px; bottom: 9px;
    background: var(--card-white);
  }
  .wordmark-back {
    color: var(--brand-blue); font-size: 28px; letter-spacing: 2px;
    flex-direction: column; gap: 12px; bottom: 0;
  }
  .details { position: absolute; left: 360px; top: 0; }
  .person-name {
    position: absolute; top: 70px; white-space: nowrap;
    font-family: "Open Sans", sans-serif; font-weight: 700;
    font-size: 29px; color: var(--ink); letter-spacing: 0.3px;
  }
  .person-title {
    position: absolute; top: 111px; white-space: nowrap;
    font-family: "Open Sans", sans-serif; font-weight: 400;
    font-size: 17px; color: var(--ink); letter-spacing: 0.3px;
  }
  .contact-list { list-style: none; position: absolute; top: 152px; }
  .contact-list li {
    display: flex; white-space: nowrap;
    font-family: "Noto Serif", serif; font-size: 15px; line-height: 26px;
    color: var(--ink); height: 31.5px;
  }
  .contact-list .label { width: 28px; flex: none; }
  .contact-list .address { line-height: 26px; height: auto; }
</style>
</head>
<body>
<main class="canvas">
  <section class="card card-front" aria-label="Card front">
    <div class="wordmark wordmark-front">
      <svg class="mark-dot" width="40" height="40" viewBox="0 0 40 40" aria-hidden="true"><circle cx="20" cy="20" r="20" fill="#ffffff"/></svg>
      <span>PELDRAX</span>
    </div>
  </section>

  <section class="card card-back" aria-label="Card back">
    <div class="logo-panel">
      <div class="wordmark wordmark-back">
        <svg class="mark-dot" width="56" height="56" viewBox="0 0 56 56" aria-hidden="true"><circle cx="28" cy="28" r="28" fill="#0093cc"/></svg>
        <span>PELDRAX</span>
      </div>
    </div>
    <div class="details">
      <h1 class="person-name">MARK HOLLAND</h1>
      <p class="person-title">General Manager</p>
      <ul class="contact-list">
        <li><span class="label">P</span><span>555-210-7788</span></li>
        <li><span class="label">E</span><span>info@peldrax.com</span></li>
        <li><span class="label">W</span><span>www.peldrax.com</span></li>
        <li class="address"><span class="label">A</span><span>48 Birch Avenue,<br>Maple Falls, AB</span></li>
      </ul>
    </div>
  </section>
</main>
</body>
</html>
```